Stayvora Waterfront Home Postcard

Hello

I have recently placed my house on Stayvora and would like to use the very nice pictures I already have available to get postcards for my guests so they have a souvenir and it also becomes a advertisement tool. Can you help me?

Thank you
Margit

Target Market(s)

Holiday makers looking for a wildlife sanctuary

Industry/Entity Type

House

Font styles to use
Script

Colors

Designer to choose colors to be used in the design.

Requirements
Must have
• Water front Home on one of the Kestrel Isles near Brisbane beautifully furnished and appointed for $30/night (on the basis of x4 people sharing) sleeps max. 6 people

Book through Stayvora: www.stayvora.com.au/rooms/4093271 and your friendly host will give you more details
Nice to have
• If it is possible to also have some of the other pictures

```html
<!DOCTYPE html>
<html lang="en">
<head>
<meta charset="utf-8">
<title>Stayvora Waterfront Home Postcard</title>
<link href="https://fonts.googleapis.com/css2?family=Raleway:wght@400;500;700;800&display=swap" rel="stylesheet">
<style>
  :root {
    --backdrop: #e4e4e4;
    --card: #ffffff;
    --band-warm: #eee3da;
    --title-red: #d0112b;
    --body-grey: #6b625d;
    --ink-dark: #3a2a24;
    --ribbon: #4a2d24;
    --ribbon-text: #ffffff;
  }
  * { box-sizing: border-box; margin: 0; padding: 0; }
  html, body {
    width: 1200px; height: 800px; overflow: hidden;
    background: var(--backdrop);
    font-family: "Raleway", Arial, sans-serif;
  }
  .postcard {
    position: absolute; left: 30px; top: 42px;
    width: 1140px; height: 716px;
    background: linear-gradient(90deg, var(--card) 0%, var(--card) 55%, var(--band-warm) 100%);
    box-shadow: 0 4px 18px rgba(0,0,0,.18);
  }
  .photo { position: absolute; }
  .photo--living {
    left: 36px; top: 16px; width: 784px; height: 463px;
    background:
      linear-gradient(180deg, rgba(255,255,255,0) 55%, rgba(200,170,140,.55) 100%),
      linear-gradient(90deg, #a98cc0 0%, #b79bc7 18%, #e8d77a 38%, #d2693c 62%, #e4cf74 85%, #c9b06a 100%);
  }
  .photo--patio {
    left: 830px; top: 16px; width: 274px; height: 148px;
    background: linear-gradient(160deg, #5e6b4a 0%, #8a6e56 50%, #6b4a3c 100%);
  }
  .photo--bedroom {
    left: 830px; top: 173px; width: 274px; height: 148px;
    background: linear-gradient(135deg, #e2c56a 0%, #b46a3a 45%, #d8cfc4 70%, #c23a3a 100%);
  }
  .photo--kitchen {
    left: 830px; top: 331px; width: 274px; height: 148px;
    background: linear-gradient(180deg, #d4693f 0%, #e0c774 45%, #d9d2c8 75%, #b8946a 100%);
  }
  .listing {
    position: absolute; left: 36px; top: 494px; width: 690px;
  }
  .listing__title {
    color: var(--title-red);
    font-weight: 800; font-size: 25px; line-height: 27px;
    text-transform: uppercase; letter-spacing: .2px;
  }
  .listing__text {
    margin-top: 4px;
    color: var(--body-grey);
    font-size: 19px; line-height: 25px; font-weight: 500;
    white-space: nowrap;
  }
  .booking {
    position: absolute; left: 16px; top: 662px;
    width: 664px; height: 34px;
  }
  .booking svg { position: absolute; inset: 0; }
  .booking__text {
    position: relative;
    padding-left: 20px; line-height: 34px;
    color: var(--ribbon-text); font-size: 18px; font-weight: 500;
  }
  .booking__text strong { font-weight: 700; }
  .price {
    position: absolute; left: 760px; top: 500px; width: 330px;
    text-align: center; color: var(--ink-dark);
  }
  .price__lead { font-size: 21px; font-weight: 700; }
  .price__amount { font-size: 60px; font-weight: 700; line-height: 66px; }
  .price__terms { font-size: 16px; line-height: 22px; font-weight: 500; }
</style>
</head>
<body>
  <main class="postcard">
    <div class="photo photo--living" role="img" aria-label="Photo of the open-plan living room with sofas and colourful walls"></div>
    <div class="photo photo--patio" role="img" aria-label="Photo of the veranda with a hammock"></div>
    <div class="photo photo--bedroom" role="img" aria-label="Photo of a bedroom with a red quilt"></div>
    <div class="photo photo--kitchen" role="img" aria-label="Photo of the kitchen"></div>

    <section class="listing">
      <h1 class="listing__title">Waterfront home on one of the<br>Kestrel Isles near Brisbane</h1>
      <p class="listing__text">Our beautifully designed 3 bedroom, 2 bathroom home also has a<br>very large (50m2) veranda overlooking a level lawn that takes you<br>to a little sandy beach. At high tide you can swim or launch the<br>canoe. You can also hand feed the birds as we do !</p>
    </section>

    <div class="booking">
      <svg width="664" height="34" viewBox="0 0 664 34" aria-hidden="true">
        <polygon points="0,0 664,0 646,17 664,34 0,34" fill="var(--ribbon)"/>
      </svg>
      <p class="booking__text"><strong>Book through Stayvora:</strong> www.stayvora.com.au/rooms/4093271</p>
    </div>

    <section class="price">
      <p class="price__lead">Appointed for</p>
      <p class="price__amount">$30/night</p>
      <p class="price__terms">(on the basis of x4 people sharing)<br>sleeps max. 6 people</p>
    </section>
  </main>
</body>
</html>
```